Redesign website for small print company

Vindaborgprent is a small printing company in Iceland mainly servicing Students, schools, etc. We are also doing all kind of other jobs, like business cards, book printing, brochure printing etc. We are also selling books online.
Our website is: www.vindaborgprent.is
What we are looking for is:
- Web Design (Uncoded - PSD layout only)
- Mobile friendly design, using our current color scheme: Red, green, yellow and light gray.
- Clean simple design
- Simple, light and easy to use.
- More menu Items/drop down
Industry/Entity Type
Digital Printing
Number of Pages Required
5+ page
Requirements
Must have
- Easy navigation
- Designed for mobile
- Current color scheme (see logo)
Nice to have
- Icon based products

```html
<!DOCTYPE html>
<html lang="en">
<head>
<meta charset="utf-8">
<title>Vindaborgprent – Website Layout</title>
<link href="https://fonts.googleapis.com/css2?family=Montserrat:wght@400;600;700;800&display=swap" rel="stylesheet">
<style>
:root{
  --red:#ec3a3c;
  --orange:#f7911f;
  --dark:#3b3b3d;
  --gray:#ececec;
  --mid:#d9d9d9;
  --text:#555;
  --blue:#2f7fc1;
  --yellow:#f5c518;
  --green:#3fae49;
  --grad:linear-gradient(90deg,var(--red),var(--orange));
}
*{box-sizing:border-box;margin:0;padding:0}
html,body{width:749px;height:1200px;overflow:hidden;background:#fff;font-family:'Montserrat',sans-serif;color:var(--text)}
.canvas{position:relative;width:749px;height:1200px}
.abs{position:absolute}
.tiny{font-size:3.6px;line-height:5.4px}
.micro{font-size:3px;line-height:4.6px}
.brand{font-weight:700;color:#222;font-size:7px;display:flex;align-items:center;gap:3px}
.brand i{width:7px;height:7px;background:var(--red);display:block}
.icon-btn{width:7px;height:7px;border:1px solid #777;border-radius:50%}
.soc{width:7px;height:7px;border-radius:50%;background:#333}
.hero-title{color:#fff;font-weight:800;line-height:1.15}
.pill{background:#fff;color:var(--red);border-radius:20px;font-weight:600;text-align:center}
.photo{background:linear-gradient(135deg,#2b2b2e,#121214)}
.photo-light{background:linear-gradient(135deg,#e8e8ea,#bfc3c8)}
.map{background:linear-gradient(160deg,#a9d6f5 0%,#a9d6f5 28%,#eceae4 30%,#e4e1d8 100%)}
.section-title{font-weight:800;color:#222;text-align:center}
.rule{display:flex;height:1.5px;width:28px}
.rule span{flex:1}
.feature-label{font-size:4px;font-weight:600;color:#444;text-align:center}
.field{border:1px solid #bbb;border-radius:10px;background:#fff;font-size:3px;color:#999;padding:2px 6px}
.btn-outline{border:1px solid #999;border-radius:10px;font-size:3.6px;font-weight:700;color:#444;text-align:center;background:#fff}
.tile{position:absolute}
.dot{width:14px;height:14px;border-radius:50%;background:var(--orange);display:flex;align-items:center;justify-content:center}
.foot-text{font-size:4.4px;font-weight:600;color:#333;text-align:center}
</style>
</head>
<body>
<div class="canvas">

<!-- ===== DESKTOP ===== -->
<header class="abs" style="left:79px;top:20px;width:342px;height:28px;background:var(--gray)">
  <div class="brand abs" style="left:48px;top:10px"><i></i>VINDABORGPRENT</div>
  <div class="abs" style="left:128px;top:8px;width:108px;height:12px;border:1px solid var(--red);background:#fff;font-size:3px;color:#999;padding:3px 5px">All ▾ &nbsp; Search...</div>
  <div class="abs" style="left:224px;top:8px;width:12px;height:12px;background:var(--red)"></div>
  <div class="abs icon-btn" style="left:273px;top:11px"></div>
  <div class="abs icon-btn" style="left:285px;top:11px;border-radius:1px"></div>
</header>
<nav class="abs" style="left:79px;top:48px;width:342px;height:17px;background:#fff">
  <div class="abs micro" style="left:49px;top:6px;display:flex;gap:17px;color:#333"><span>Home</span><span>Services</span><span>Submission of works</span><span>About us</span></div>
  <div class="abs" style="left:251px;top:5px;display:flex;gap:3px"><i class="soc"></i><i class="soc" style="background:var(--orange)"></i><i class="soc"></i><i class="soc"></i></div>
</nav>
<section class="abs" style="left:79px;top:65px;width:342px;height:150px;background:var(--grad)">
  <div class="abs photo" role="img" aria-label="Black magazine and mock-up brochures on a desk" style="left:0;top:16px;width:173px;height:118px"></div>
  <div class="abs hero-title" style="left:143px;top:42px;font-size:17px">Engar Ahyggjur<br><span style="padding-left:8px">....Petta Reddast</span></div>
  <div class="abs pill" style="left:226px;top:104px;width:48px;height:11px;font-size:3.8px;line-height:11px">Order Now</div>
</section>
<section class="abs" style="left:79px;top:215px;width:342px;height:47px;background:var(--gray)">
  <div class="abs" style="left:0;top:0;width:133px;height:47px;background:var(--dark)">
    <p class="abs micro" style="left:49px;top:10px;width:80px;color:#eee">Vindaborgprent is a small printing house near the campus, serving students, school staff and the general public with fast, friendly printing.</p>
  </div>
  <svg class="abs" style="left:207px;top:13px" width="22" height="16" viewBox="0 0 22 16"><rect x="1" y="4" width="20" height="11" rx="1" fill="var(--blue)"/><rect x="8" y="1" width="6" height="4" fill="none" stroke="var(--blue)" stroke-width="1.5"/><rect x="9.5" y="8" width="3" height="2" fill="#fff"/></svg>
  <svg class="abs" style="left:275px;top:12px" width="18" height="16" viewBox="0 0 18 16"><ellipse cx="9" cy="8" rx="8.5" ry="7.5" fill="var(--yellow)"/><circle cx="5" cy="6" r="1.6" fill="var(--red)"/><circle cx="9" cy="4" r="1.6" fill="var(--blue)"/><circle cx="13" cy="6" r="1.6" fill="var(--green)"/><circle cx="7" cy="11" r="1.6" fill="#fff"/></svg>
  <svg class="abs" style="left:343px;top:12px" width="12" height="18" viewBox="0 0 12 18"><circle cx="6" cy="6" r="5.5" fill="var(--green)"/><rect x="3.5" y="11" width="5" height="5" fill="var(--yellow)"/></svg>
  <div class="abs feature-label" style="left:197px;top:34px;width:42px">SENDA VERK</div>
  <div class="abs feature-label" style="left:263px;top:34px;width:42px">HANNA VERK</div>
  <div class="abs feature-label" style="left:328px;top:34px;width:42px">FA TILBOD</div>
  <div class="abs" style="left:133px;bottom:0;width:209px;height:2px;display:flex"><span style="flex:1;background:var(--blue)"></span><span style="flex:1;background:var(--yellow)"></span><span style="flex:1;background:var(--green)"></span></div>
</section>

<div class="abs photo-light" role="img" aria-label="Folded blue flyer mock-up" style="left:100px;top:298px;width:142px;height:122px;background:linear-gradient(135deg,#fff,#d4e6f4 40%,#3a9ad9 70%,#e9e9e9)"></div>
<div class="abs section-title" style="left:263px;top:294px;font-size:8px">ABOUT US</div>
<div class="abs rule" style="left:263px;top:305px"><span style="background:var(--red)"></span><span style="background:var(--yellow)"></span><span style="background:var(--green)"></span><span style="background:var(--blue)"></span></div>
<div class="abs micro" style="left:263px;top:316px;width:110px">
  <p>Vindaborgprent is a print shop located on the campus, specialised in serving school staff as well as general public printing.</p><br>
  <p>Higher education publishes seminars and first-class textbooks for courses, theses for lessons and many smaller pieces for students, teachers and organisations: brochures, reports, business cards, books and scanning.</p><br>
  <p>Vindaborgprent is a tailored print shop holding an eco-label, and is well known across the country.</p><br>
  <p>The shop is located at the corner of Lindargata and Hafnargata.</p>
</div>

<div class="abs section-title" style="left:200px;top:434px;width:100px;font-size:8px">CATALOG</div>
<div class="abs rule" style="left:236px;top:445px"><span style="background:var(--red)"></span><span style="background:var(--yellow)"></span><span style="background:var(--green)"></span><span style="background:var(--blue)"></span></div>
<div class="abs micro" style="left:143px;top:454px;display:flex;gap:12px;align-items:center;color:#555">
  <span style="background:var(--red);color:#fff;border-radius:4px;padding:0 4px">All</span><span>Essays</span><span>Business cards</span><span>Pamphlets</span><span>Book Printing</span><span>Posters</span><span>Textbooks</span>
</div>
<div class="tile photo-light" role="img" aria-label="Printed forms and papers" style="left:128px;top:471px;width:56px;height:42px"></div>
<div class="tile" role="img" aria-label="Book cover with bold title" style="left:190px;top:471px;width:57px;height:42px;background:linear-gradient(135deg,#c9302c,#1c2a4a)"></div>
<div class="tile" role="img" aria-label="Assorted printed magazines" style="left:253px;top:471px;width:57px;height:42px;background:linear-gradient(135deg,#e0b030,#2d5a8a)"></div>
<div class="tile photo-light" role="img" aria-label="Greeting card with red bird" style="left:316px;top:471px;width:56px;height:42px;background:linear-gradient(135deg,#f2f2f2,#e05050)"></div>
<div class="tile photo-light" role="img" aria-label="Textbook cover" style="left:128px;top:519px;width:56px;height:94px;background:linear-gradient(160deg,#8fbf6a,#efefef 50%,#d65a7a)"></div>
<div class="tile photo-light" role="img" aria-label="Illustrated card" style="left:190px;top:519px;width:57px;height:94px;background:linear-gradient(160deg,#f3f3f3,#e6e6e6 50%,#e14040)"></div>
<div class="tile photo" role="img" aria-label="Stacked black booklets" style="left:253px;top:519px;width:57px;height:43px"></div>
<div class="tile" role="img" aria-label="Spread of printed brochures" style="left:253px;top:568px;width:57px;height:45px;background:linear-gradient(135deg,#3a6fa8,#e9e9e9)"></div>
<div class="tile photo-light" role="img" aria-label="Illustrated book cover" style="left:316px;top:519px;width:56px;height:94px;background:linear-gradient(160deg,#f4f4f4,#cfe3b0 60%,#e2a23a)"></div>

<section class="abs" style="left:79px;top:630px;width:342px;height:165px;background:var(--mid)">
  <div class="abs" style="left:49px;top:20px;width:244px;height:123px;background:#fff;box-shadow:0 1px 3px rgba(0,0,0,.15)">
    <div class="abs" style="left:0;top:0;width:82px;height:123px;background:var(--grad);padding:16px 7px;color:#fff">
      <div style="font-size:6px;font-weight:800;line-height:7px">SUBMISSION OF<br>WORKS</div>
      <p class="micro" style="margin-top:6px">There are various ways to send us a project: submit content directly, on paper, or on a disk, whichever suits you best.</p><br>
      <p class="micro">A common way is to send a project by e-mail to verk@vindaborgprent.is. Large files can be uploaded to our data server below.</p>
    </div>
    <div class="abs field" style="left:96px;top:16px;width:68px;height:11px">Name</div>
    <div class="abs field" style="left:170px;top:16px;width:68px;height:11px">Email</div>
    <div class="abs field" style="left:96px;top:33px;width:142px;height:33px;border-radius:5px">Message</div>
    <div class="abs" style="left:120px;top:74px;width:12px;height:12px;border-radius:50%;background:var(--red)"></div>
    <div class="abs micro" style="left:146px;top:77px;color:#444">DRAG FILES IN THIS WINDOW TO SEND</div>
    <div class="abs btn-outline" style="left:118px;top:96px;width:64px;height:11px;line-height:9px;border-radius:10px 0 0 10px">EXIT</div>
    <div class="abs btn-outline" style="left:182px;top:96px;width:64px;height:11px;line-height:9px;border-radius:0 10px 10px 0">SEND</div>
  </div>
</section>
<div class="abs map" role="img" aria-label="Street map showing the shop location" style="left:79px;top:795px;width:342px;height:120px"></div>
<svg class="abs" style="left:244px;top:871px" width="8" height="11" viewBox="0 0 8 11"><path d="M4 11 C4 11 0 6 0 4 A4 4 0 0 1 8 4 C8 6 4 11 4 11Z" fill="var(--red)"/></svg>

<footer>
  <div class="abs dot" style="left:157px;top:930px"><svg width="7" height="7" viewBox="0 0 7 7"><path d="M1 1 L2.5 1 L3 2.5 L2.3 3 A4 4 0 0 0 4 4.7 L4.5 4 L6 4.5 L6 6 A5 5 0 0 1 1 1Z" fill="#fff"/></svg></div>
  <div class="abs dot" style="left:241px;top:930px"><svg width="7" height="5" viewBox="0 0 7 5"><rect width="7" height="5" fill="#fff"/><path d="M0 0 L3.5 3 L7 0" fill="none" stroke="var(--orange)" stroke-width=".8"/></svg></div>
  <div class="abs dot" style="left:333px;top:929px"><svg width="6" height="8" viewBox="0 0 6 8"><path d="M3 8 C3 8 0 4.5 0 3 A3 3 0 0 1 6 3 C6 4.5 3 8 3 8Z" fill="#fff"/></svg></div>
  <div class="abs" style="left:213px;top:925px;width:1px;height:42px;background:#ccc"></div>
  <div class="abs" style="left:298px;top:925px;width:1px;height:42px;background:#ccc"></div>
  <div class="abs foot-text" style="left:134px;top:950px;width:60px">555 0142</div>
  <div class="abs foot-text" style="left:205px;top:950px;width:90px">VERK@VINDABORGPRENT.IS</div>
  <div class="abs foot-text" style="left:300px;top:947px;width:82px">VINDABORGPRENT KT:<br>540219-2290</div>
  <div class="abs" style="left:234px;top:972px;width:14px;height:9px;background:#333;border-radius:1px"></div>
  <div class="abs" style="left:252px;top:972px;width:14px;height:9px;background:#333;border-radius:1px"></div>
  <div class="abs micro" style="left:180px;top:988px;width:140px;text-align:center;color:#777">© 2018 Vindaborgprent. All rights reserved.</div>
</footer>

<!-- ===== MOBILE ===== -->
<header class="abs" style="left:510px;top:20px;width:165px;height:27px;background:var(--gray)">
  <div class="brand abs" style="left:14px;top:10px;font-size:6px"><i style="width:6px;height:6px"></i>VINDABORGPRENT</div>
  <div class="abs icon-btn" style="left:108px;top:11px;width:6px;height:6px"></div>
  <div class="abs icon-btn" style="left:119px;top:11px;width:6px;height:6px"></div>
  <div class="abs icon-btn" style="left:130px;top:11px;width:6px;height:6px;border-radius:1px"></div>
  <div class="abs" style="left:145px;top:10px;width:8px;height:6px;border-top:1.5px solid #222;border-bottom:1.5px solid #222"></div>
  <div class="abs" style="left:145px;top:12.2px;width:8px;height:1.5px;background:#222"></div>
</header>
<section class="abs" style="left:510px;top:47px;width:165px;height:95px;background:var(--grad)">
  <div class="abs photo" role="img" aria-label="Black magazine and mock-up brochures" style="left:0;top:16px;width:95px;height:65px"></div>
  <div class="abs hero-title" style="left:49px;top:27px;font-size:11px">Engar Ahyggjur<br><span style="padding-left:4px">....Petta Reddast</span></div>
  <div class="abs pill" style="left:110px;top:67px;width:42px;height:9px;font-size:3.2px;line-height:9px">Order Now</div>
</section>
<section class="abs" style="left:510px;top:142px;width:165px;height:47px;background:var(--dark);border-bottom:2px solid var(--red)">
  <p class="abs micro" style="left:18px;top:13px;width:130px;color:#eee;text-align:center">Vindaborgprent is a small printing house near the campus, serving students, school staff and the general public with fast, friendly printing.</p>
</section>
<div class="abs" style="left:510px;top:189px;width:165px;height:73px;background:var(--gray);border-bottom:2px solid var(--blue)">
  <svg class="abs" style="left:72px;top:18px" width="22" height="16" viewBox="0 0 22 16"><rect x="1" y="4" width="20" height="11" rx="1" fill="var(--blue)"/><rect x="8" y="1" width="6" height="4" fill="none" stroke="var(--blue)" stroke-width="1.5"/><rect x="9.5" y="8" width="3" height="2" fill="#fff"/></svg>
  <div class="abs feature-label" style="left:0;top:48px;width:165px">SENDA VERK</div>
</div>
<div class="abs" style="left:510px;top:265px;width:165px;height:73px;background:var(--gray);border-bottom:2px solid var(--yellow)">
  <svg class="abs" style="left:73px;top:17px" width="20" height="18" viewBox="0 0 18 16"><ellipse cx="9" cy="8" rx="8.5" ry="7.5" fill="var(--yellow)"/><circle cx="5" cy="6" r="1.6" fill="var(--red)"/><circle cx="9" cy="4" r="1.6" fill="var(--blue)"/><circle cx="13" cy="6" r="1.6" fill="var(--green)"/><circle cx="7" cy="11" r="1.6" fill="#fff"/></svg>
  <div class="abs feature-label" style="left:0;top:48px;width:165px">SENDA VERK</div>
</div>
<div class="abs" style="left:510px;top:340px;width:165px;height:73px;background:var(--gray);border-bottom:2px solid var(--green)">
  <svg class="abs" style="left:77px;top:12px" width="12" height="20" viewBox="0 0 12 18"><circle cx="6" cy="6" r="5.5" fill="var(--green)"/><rect x="3.5" y="11" width="5" height="5" fill="var(--yellow)"/></svg>
  <div class="abs feature-label" style="left:0;top:46px;width:165px">SENDA VERK</div>
</div>

<div class="abs" role="img" aria-label="Folded blue flyer mock-up" style="left:546px;top:426px;width:90px;height:85px;background:linear-gradient(135deg,#fff,#d4e6f4 40%,#3a9ad9 70%,#e9e9e9)"></div>
<div class="abs section-title" style="left:510px;top:529px;width:165px;font-size:7.5px">ABOUT US</div>
<div class="abs rule" style="left:579px;top:539px"><span style="background:var(--red)"></span><span style="background:var(--yellow)"></span><span style="background:var(--green)"></span><span style="background:var(--blue)"></span></div>
<div class="abs micro" style="left:520px;top:550px;width:145px;text-align:center">
  <p>Vindaborgprent is a print shop located on the campus, specialised in serving school staff as well as general public printing.</p><br>
  <p>Higher education publishes seminars and first-class textbooks for courses, theses for lessons and many smaller pieces for students, teachers and organisations: brochures, reports, business cards, books and scanning.</p><br>
  <p>Vindaborgprent is a tailored print shop holding an eco-label, and is well known across the country.</p><br>
  <p>The shop is located at the corner of Lindargata and Hafnargata.</p>
</div>
<div class="abs section-title" style="left:510px;top:656px;width:165px;font-size:7.5px">CATALOG</div>
<div class="abs rule" style="left:579px;top:666px"><span style="background:var(--red)"></span><span style="background:var(--yellow)"></span><span style="background:var(--green)"></span><span style="background:var(--blue)"></span></div>
<div class="abs" style="left:526px;top:678px;width:133px;height:20px;background:var(--gray);font-size:4px;color:#555;padding:6px 18px">All<span style="position:absolute;right:14px;top:5px;width:5px;height:5px;border-right:1px solid #333;border-bottom:1px solid #333;transform:rotate(45deg)"></span></div>
<div class="abs" role="img" aria-label="Book cover with bold title among magazines" style="left:527px;top:712px;width:131px;height:83px;background:linear-gradient(135deg,#d7d9dc,#c9302c 45%,#1c2a4a 60%,#d7d9dc)"></div>
<div class="abs" style="left:583px;top:800px;display:flex;gap:1.5px">
  <i style="width:3px;height:3px;border-radius:50%;background:#333"></i><i style="width:3px;height:3px;border-radius:50%;border:.6px solid #333"></i><i style="width:3px;height:3px;border-radius:50%;border:.6px solid #333"></i><i style="width:3px;height:3px;border-radius:50%;border:.6px solid #333"></i>
</div>
<section class="abs" style="left:510px;top:815px;width:165px;height:86px;background:var(--grad);color:#fff;text-align:center;padding:12px 14px">
  <div style="font-size:5.5px;font-weight:800">SUBMISSION OF WORKS</div>
  <p class="micro" style="margin-top:6px">There are various ways to send us a project: submit content directly, on paper, or on a disk, whichever suits you best.</p><br>
  <p class="micro">A common way is to send a project by e-mail to verk@vindaborgprent.is. Large files can be uploaded to our data server below.</p>
</section>
<div class="abs field" style="left:522px;top:916px;width:68px;height:11px">Name</div>
<div class="abs field" style="left:594px;top:916px;width:68px;height:11px">Email</div>
<div class="abs field" style="left:522px;top:936px;width:140px;height:33px;border-radius:5px">Message</div>
<div class="abs" style="left:542px;top:978px;width:12px;height:12px;border-radius:50%;background:var(--red)"></div>
<div class="abs micro" style="left:580px;top:982px;color:#444">DRAG FILES IN THIS WINDOW TO SEND</div>
<div class="abs btn-outline" style="left:538px;top:997px;width:54px;height:11px;line-height:9px;border-radius:10px 0 0 10px">EXIT</div>
<div class="abs btn-outline" style="left:593px;top:997px;width:54px;height:11px;line-height:9px;border-radius:0 10px 10px 0">SEND</div>
<div class="abs map" role="img" aria-label="Street map showing the shop location" style="left:510px;top:1022px;width:165px;height:119px"></div>
<svg class="abs" style="left:613px;top:1086px" width="8" height="11" viewBox="0 0 8 11"><path d="M4 11 C4 11 0 6 0 4 A4 4 0 0 1 8 4 C8 6 4 11 4 11Z" fill="var(--red)"/></svg>
<footer class="abs" style="left:510px;top:1141px;width:165px;height:43px;background:var(--mid)">
  <div class="abs" style="left:46px;top:15px;display:flex;gap:6px">
    <i class="soc" style="width:13px;height:13px"></i><i class="soc" style="width:13px;height:13px;background:var(--orange)"></i><i class="soc" style="width:13px;height:13px"></i><i class="soc" style="width:13px;height:13px"></i>
  </div>
</footer>

</div>
</body>
</html>
```